Laser hair removal, Cellulite Reduction PDT Led Light Therapy & Hot Stone Massage

I need a business card design for a new business based in Sydney Australia. Our treatments include Laser Hair Removal, Cellulite & Fat Reduction,
PDT LED light rejuvenation therapy, and Hot Stone Massage. The main Medical Aesthetician has a Nursing background of 12yrs and is also a Registered Nurse .All treatments are safe painless and effective using the latest Technology.
It is located at 4/17 Marlow Crescent, Pellham Downs NSW Mbl: 0438 516 904
Watch for our Specials

Target Market(s)

Male & Females

Industry/Entity Type

Business

Contact Information for Business Card

Body Treatments from Head to toe

Colors
33b8a4
86cfc6
00a990
a64599
b868aa
d3a5cc

Requirements
Must have
• All my Treatments on the card and a nice call to attention statement
• Must be colourful in Blue or Green hues
Nice to have
• A nice image of a male & female together
Should not have
• Should not look overcrowded with words

```html
<!DOCTYPE html>
<html lang="en">
<head>
<meta charset="utf-8">
<title>Velora Body – Business Card</title>
<link rel="stylesheet" href="https://fonts.googleapis.com/css2?family=Caveat:wght@400&family=Kurale&display=swap">
<style>
  :root {
    --page-bg: #ececec;
    --card-bg: #f7f7f8;
    --band-blue: #6a9cff;
    --band-lilac: #b6b2ff;
    --band-violet: #6c6cff;
    --band-violet-light: #9c90ff;
    --brand-ink: #5b8ef0;
    --ink-violet: #6a5fe0;
    --ink-white: #ffffff;
  }
  * { margin: 0; padding: 0; box-sizing: border-box; }
  html, body { width: 1200px; height: 1000px; overflow: hidden; }
  body { background: var(--page-bg); position: relative; font-family: "Kurale", serif; }

  .card {
    position: absolute;
    width: 712px;
    height: 386px;
    background: linear-gradient(160deg, #ffffff 0%, var(--card-bg) 55%, #efeff1 100%);
    overflow: hidden;
  }
  .card--front { left: 130px; top: 79px; }
  .card--back { left: 396px; top: 537px; }

  .band {
    position: absolute;
    left: 0;
    width: 100%;
    background: linear-gradient(110deg,
      var(--band-blue) 0%, var(--band-lilac) 22%, var(--band-blue) 45%,
      var(--band-lilac) 68%, var(--band-blue) 85%, var(--band-lilac) 100%);
  }
  .band--top { top: 0; height: 38px; }
  .band--bottom { bottom: 0; height: 43px; }

  .brand {
    position: absolute;
    top: 82px;
    width: 100%;
    text-align: center;
    font-family: "Kurale", serif;
    font-weight: 400;
    font-size: 54px;
    line-height: 1;
    color: var(--brand-ink);
  }

  .contact {
    position: absolute;
    top: 213px;
    width: 100%;
    list-style: none;
    text-align: center;
    color: var(--ink-violet);
    font-size: 18px;
  }
  .contact li { height: 33px; line-height: 33px; }
  .contact li + li + li { margin-top: 2px; }
  .contact svg { width: 18px; height: 18px; vertical-align: -3px; margin-right: 6px; fill: var(--ink-violet); }

  .treatments-title {
    position: absolute;
    top: 70px;
    width: 100%;
    text-align: center;
    font-family: "Caveat", cursive;
    font-weight: 400;
    font-size: 40px;
    line-height: 52px;
    color: var(--ink-violet);
  }
  .treatments-band {
    position: absolute;
    left: 0;
    top: 137px;
    width: 100%;
    height: 128px;
    background: linear-gradient(110deg,
      var(--band-violet) 0%, var(--band-violet-light) 30%, var(--band-violet) 50%,
      var(--band-violet-light) 75%, var(--band-violet) 100%);
  }
  .treatments-list {
    list-style: none;
    padding-top: 7px;
    text-align: center;
    color: var(--ink-white);
    font-size: 22px;
    line-height: 28.6px;
    letter-spacing: 0.3px;
  }
  .specials {
    position: absolute;
    top: 272px;
    width: 100%;
    text-align: center;
    font-family: "Caveat", cursive;
    font-weight: 400;
    font-size: 46px;
    line-height: 58px;
    color: var(--ink-violet);
  }
</style>
</head>
<body>
  <section class="card card--front" aria-label="Business card front">
    <div class="band band--top"></div>
    <h1 class="brand">Velora Body</h1>
    <ul class="contact">
      <li><svg viewBox="0 0 24 24" aria-hidden="true"><path d="M6.6 10.8a15.1 15.1 0 0 0 6.6 6.6l2.2-2.2a1 1 0 0 1 1-.25 11.4 11.4 0 0 0 3.6.57 1 1 0 0 1 1 1V20a1 1 0 0 1-1 1A17 17 0 0 1 3 4a1 1 0 0 1 1-1h3.5a1 1 0 0 1 1 1c0 1.25.2 2.45.57 3.57a1 1 0 0 1-.25 1z"/></svg>0438 516 904</li>
      <li><svg viewBox="0 0 24 24" aria-hidden="true"><path d="M3 6h18l-9 6.5z"/><path d="M2 7.5 12 14.5 22 7.5V19H2z"/></svg>hello@velorabody.com.au</li>
      <li><svg viewBox="0 0 24 24" aria-hidden="true"><path d="M12 2 1 12h3v9h6v-6h4v6h6v-9h3z"/></svg>4/17 Marlow Crescent, Pellham Downs NSW</li>
    </ul>
    <div class="band band--bottom"></div>
  </section>

  <section class="card card--back" aria-label="Business card back">
    <div class="band band--top"></div>
    <h2 class="treatments-title">Our Treatments:</h2>
    <div class="treatments-band">
      <ul class="treatments-list">
        <li>Laser Hair Removal</li>
        <li>Cellulite &amp; Fat Reduction</li>
        <li>PDT LED Light Rejuvenation Therapy</li>
        <li>Hot Stone Massage</li>
      </ul>
    </div>
    <p class="specials">Watch for our Specials</p>
    <div class="band band--bottom"></div>
  </section>
</body>
</html>
```